Book Cover Design

Design with title UNWAVERING
Subtitle: Ways to Kindle the Spark of Resolve
Author Name: Carla Jean Morrow
Put DAILY MERIDIAN BESTSELLER at top
Shimmer design, see inspirational images attached

```html
<!DOCTYPE html>
<html lang="en">
<head>
<meta charset="utf-8">
<title>Unwavering — Carla Jean Morrow</title>
<link rel="stylesheet" href="https://fonts.googleapis.com/css2?family=Jost:wght@500;700&family=Questrial&display=swap">
<style>
  :root {
    --page: #ffffff;
    --title-ink: #1c1848;
    --subtitle-ink: #7c84a3;
    --author-ink: #111111;
    --badge: #f7941d;
    --badge-edge: #e8801a;
    --badge-ink: #2a1606;
    --sky: #98a8ee;
    --lilac: #cfaef0;
    --blush: #efc4ef;
    --aqua: #a9effb;
    --lemon: #fbf9b2;
    --mist: #ffffff;
  }
  * { margin: 0; padding: 0; box-sizing: border-box; }
  html, body {
    width: 1200px;
    height: 1200px;
    overflow: hidden;
    background: var(--page);
  }
  .canvas {
    position: relative;
    width: 1200px;
    height: 1200px;
  }
  .book-cover {
    position: absolute;
    left: 272px;
    top: 103px;
    width: 655px;
    height: 994px;
    overflow: hidden;
    background:
      radial-gradient(ellipse 40% 28% at 88% 86%, var(--mist) 0%, rgba(255,255,255,0) 100%),
      radial-gradient(ellipse 45% 28% at 24% 88%, var(--lemon) 0%, rgba(251,249,178,0) 100%),
      radial-gradient(ellipse 40% 30% at 94% 58%, var(--lemon) 0%, rgba(251,249,178,0) 100%),
      radial-gradient(ellipse 36% 30% at 50% 68%, var(--aqua) 0%, rgba(169,239,251,0) 100%),
      radial-gradient(ellipse 30% 22% at 0% 62%, #c9f7e6 0%, rgba(201,247,230,0) 100%),
      radial-gradient(ellipse 34% 28% at 16% 44%, var(--blush) 0%, rgba(239,196,239,0) 100%),
      radial-gradient(ellipse 34% 26% at 98% 34%, #d0a8f0 0%, rgba(208,168,240,0) 100%),
      radial-gradient(ellipse 60% 26% at 50% 6%, var(--sky) 0%, rgba(152,168,238,0) 100%),
      linear-gradient(180deg, #b6b4ef 0%, #d6d3f2 40%, #dcf2f6 70%, #fbfbe8 100%);
  }
  .cover-foil {
    position: absolute;
    inset: 0;
    width: 100%;
    height: 100%;
    opacity: 0.32;
    mix-blend-mode: overlay;
  }
  .bestseller-seal {
    position: absolute;
    left: 36px;
    top: 27px;
    width: 50px;
    height: 50px;
    border-radius: 50%;
    background: var(--badge);
    border: 2px solid var(--badge-edge);
    display: flex;
    align-items: center;
    justify-content: center;
    text-align: center;
    font-family: "Jost", sans-serif;
    font-weight: 700;
    font-size: 6.5px;
    line-height: 1.15;
    letter-spacing: 0.2px;
    text-transform: uppercase;
    color: var(--badge-ink);
  }
  .title {
    position: absolute;
    top: 184px;
    left: 0;
    width: 100%;
    text-align: center;
    font-family: "Jost", sans-serif;
    font-weight: 700;
    font-size: 50px;
    line-height: 1;
    letter-spacing: 15px;
    padding-left: 15px;
    text-transform: uppercase;
    color: var(--title-ink);
  }
  .subtitle {
    position: absolute;
    top: 273px;
    left: 0;
    width: 100%;
    text-align: center;
    font-family: "Questrial", sans-serif;
    font-size: 26px;
    line-height: 37px;
    letter-spacing: 3px;
    text-transform: uppercase;
    color: var(--subtitle-ink);
  }
  .author {
    position: absolute;
    top: 941px;
    left: 0;
    width: 100%;
    text-align: center;
    font-family: "Jost", sans-serif;
    font-weight: 500;
    font-size: 14px;
    line-height: 1;
    letter-spacing: 13px;
    padding-left: 13px;
    text-transform: uppercase;
    color: var(--author-ink);
  }
</style>
</head>
<body>
  <main class="canvas">
    <section class="book-cover" aria-label="Book cover: Unwavering by Carla Jean Morrow">
      <svg class="cover-foil" aria-hidden="true" xmlns="http://www.w3.org/2000/svg">
        <filter id="foil-grain">
          <feTurbulence type="fractalNoise" baseFrequency="0.55" numOctaves="3" seed="4" stitchTiles="stitch"/>
          <feColorMatrix type="saturate" values="0"/>
          <feComponentTransfer>
            <feFuncA type="linear" slope="1.4"/>
          </feComponentTransfer>
        </filter>
        <rect width="100%" height="100%" filter="url(#foil-grain)"/>
      </svg>
      <div class="bestseller-seal">Daily<br>Meridian<br>Bestseller</div>
      <h1 class="title">Unwavering</h1>
      <p class="subtitle">Ways to Kindle<br>the Spark of Resolve</p>
      <p class="author">Carla Jean Morrow</p>
    </section>
  </main>
</body>
</html>
```